GDFH Business Card

Looking for a business card design to incorporate our branding. We want to only use the colors listing in the Branding Package (attached).
Updates

Target Market(s)

People who need their phone or device fixed.

Industry/Entity Type

Electronics

Contact Information for Business Card

Please use:

Gadget Fix Haven LLC
4870 S Ridgecrest Pkwy
Suite 318
San Antonio, TX 78291

Wendell Thorsby, Store Manager

(210) 555-0147

Requirements
Must have
• Must include the colors that are contained within the Branding Package PDF file.

```html
<!DOCTYPE html>
<html lang="en">
<head>
<meta charset="utf-8">
<title>GDFH Business Card</title>
<link rel="stylesheet" href="https://fonts.googleapis.com/css2?family=Arimo:wght@400;700&display=swap">
<style>
  :root {
    --backdrop: #e4e5e2;
    --card: #ffffff;
    --card-edge: #f2f2f2;
    --orange: #e07a2c;
    --orange-deep: #d8691c;
    --orange-soft: #e5893f;
    --lime: #d4e06b;
    --ink-grey: #6b6d70;
    --white: #ffffff;
  }
  * { box-sizing: border-box; margin: 0; padding: 0; }
  html, body {
    width: 1200px;
    height: 800px;
    overflow: hidden;
    background: var(--backdrop);
    font-family: "Arimo", Arial, sans-serif;
  }
  .sheet {
    position: relative;
    width: 1200px;
    height: 800px;
  }
  .card {
    position: absolute;
    top: 252px;
    width: 520px;
    height: 297px;
    background: var(--card);
    box-shadow: 0 6px 18px rgba(0,0,0,0.12);
    overflow: hidden;
  }
  .card--front { left: 60px; }
  .card--back { left: 620px; background: linear-gradient(180deg, var(--card) 0%, var(--card-edge) 100%); }

  .brand {
    position: absolute;
    display: flex;
    align-items: center;
    gap: 10px;
    color: var(--orange);
    font-weight: 400;
    white-space: nowrap;
  }
  .brand__square {
    background: var(--orange);
    border-radius: 4px;
    flex: none;
  }
  .card--front .brand { left: 150px; top: 128px; font-size: 30px; }
  .card--front .brand__square { width: 34px; height: 34px; }

  .front-tab {
    position: absolute;
    right: -8px;
    top: 58px;
    width: 46px;
    height: 34px;
    background: var(--orange);
    border-radius: 6px;
  }

  .card--back .brand { left: 64px; top: 64px; font-size: 25px; }
  .card--back .brand__square { width: 28px; height: 28px; }

  .contact-band {
    position: absolute;
    left: 0;
    top: 124px;
    width: 100%;
    height: 130px;
    background: linear-gradient(90deg, var(--orange-soft) 0%, var(--orange) 50%, var(--orange-deep) 100%);
    color: var(--white);
    padding: 16px 0 0 110px;
  }
  .contact__name {
    font-weight: 700;
    font-size: 17px;
    letter-spacing: 0.5px;
    text-transform: uppercase;
  }
  .contact__title { font-size: 13px; margin-top: 3px; }
  .contact__phone { font-size: 11px; margin-top: 12px; }
  .contact__address { font-size: 10px; margin-top: 14px; }
</style>
</head>
<body>
  <main class="sheet">
    <section class="card card--front" aria-label="Business card front">
      <div class="brand">
        <span class="brand__square"></span>
        <span class="brand__name">Gadget Fix Haven</span>
      </div>
      <span class="front-tab"></span>
    </section>

    <section class="card card--back" aria-label="Business card back">
      <div class="brand">
        <span class="brand__square"></span>
        <span class="brand__name">Gadget Fix Haven</span>
      </div>
      <div class="contact-band">
        <p class="contact__name">Wendell Thorsby</p>
        <p class="contact__title">Store Manager</p>
        <p class="contact__phone">(210) 555-0147</p>
        <p class="contact__address">4870 S Ridgecrest Pkwy Suite 318 San Antonio, TX 78291</p>
      </div>
    </section>
  </main>
</body>
</html>
```